Wadi Alsafeer
Wadi Alsafeer - Construction
Creative Brief
Simple
Salem Dabbagh
CEO
Locality 428 - Alley 17 - House 9 Al Dhaheera - Baghdad - Iraq
ceo@wadialsafeer.com
www.wadialsafeer.com
rokba72x rokba72x
i uploaded the final files so you all can work now with it and very soon I'll chose a winner
and i wont you to make these changes in the latter head only: 1- add the address in Arabic language ( محلة 428 - زقاق 17 - دار 9) and 2- change the e-mail into ( info@wadialsafeer.com ) thank you
Hello , great job all i just wont you to add the name and title in English and Arabic language in the businesses cards only, ( name in Arabic : سالم دباغ) and the title(CEO) in Arabic ( المدير المفوض) Regards,

```html
<!DOCTYPE html>
<html lang="en">
<head>
<meta charset="utf-8">
<title>Wadi Alsafeer – Business Card</title>
<link rel="stylesheet" href="https://fonts.googleapis.com/css2?family=Open+Sans:wght@400;600;700&family=Noto+Sans+Arabic:wght@400;600&display=swap">
<style>
  :root {
    --page-bg: #e6e7ea;
    --card-bg: #ffffff;
    --brand-blue: #1f8ad8;
    --brand-grey: #55575b;
    --text-dark: #3a3c40;
    --text-muted: #55585d;
  }
  * { margin: 0; padding: 0; box-sizing: border-box; }
  html, body {
    width: 1200px;
    height: 901px;
    overflow: hidden;
    background: var(--page-bg);
    font-family: "Open Sans", Arial, sans-serif;
  }
  .canvas {
    position: relative;
    width: 1200px;
    height: 901px;
    display: flex;
    align-items: center;
    justify-content: center;
  }
  .business-card {
    position: relative;
    width: 900px;
    height: 520px;
    background: var(--card-bg);
    border-radius: 34px;
    overflow: hidden;
    box-shadow: 0 10px 30px rgba(0,0,0,0.12);
  }
  .card-shapes {
    position: absolute;
    inset: 0;
    width: 100%;
    height: 100%;
  }
  .brand {
    position: absolute;
    left: 70px;
    top: 92px;
    display: flex;
    align-items: center;
    gap: 14px;
  }
  .brand-mark {
    width: 34px;
    height: 34px;
    background: var(--brand-grey);
  }
  .brand-name {
    font-size: 30px;
    font-weight: 700;
    color: var(--brand-blue);
    letter-spacing: 0.5px;
  }
  .person {
    position: absolute;
    left: 505px;
    top: 160px;
  }
  .person-name {
    font-size: 27px;
    font-weight: 600;
    color: var(--brand-blue);
    letter-spacing: 0.5px;
    text-transform: uppercase;
    line-height: 36px;
  }
  .person-title {
    font-size: 20px;
    color: var(--text-dark);
    line-height: 28px;
  }
  .arabic {
    font-family: "Noto Sans Arabic", "Open Sans", sans-serif;
    direction: rtl;
    text-align: left;
    unicode-bidi: plaintext;
  }
  .person-name.arabic {
    font-size: 24px;
    line-height: 38px;
    margin-top: 4px;
  }
  .person-title.arabic {
    font-size: 18px;
    line-height: 30px;
  }
  .address {
    position: absolute;
    left: 70px;
    top: 245px;
    font-size: 21px;
    line-height: 32px;
    font-style: normal;
    color: var(--text-dark);
  }
  .contacts {
    position: absolute;
    left: 70px;
    top: 350px;
    list-style: none;
  }
  .contact-item {
    display: flex;
    align-items: center;
    gap: 14px;
    font-size: 19px;
    line-height: 30px;
    color: var(--text-muted);
  }
  .contact-icon {
    width: 18px;
    height: 18px;
    flex: none;
  }
</style>
</head>
<body>
<main class="canvas">
  <section class="business-card">
    <svg class="card-shapes" viewBox="0 0 900 520" aria-hidden="true">
      <path class="corner-grey" d="M770 0 L900 0 L900 120 C875 70 830 28 770 0 Z" fill="var(--brand-grey)"/>
      <path class="side-band" d="M700 0 C820 30 900 140 900 270 L900 520 L770 520 C870 420 870 170 700 0 Z" fill="var(--brand-blue)"/>
      <path class="side-band-edge" d="M700 0 C870 170 870 420 770 520" fill="none" stroke="#ffffff" stroke-width="6"/>
    </svg>

    <div class="brand">
      <span class="brand-mark"></span>
      <span class="brand-name">Wadi Alsafeer</span>
    </div>

    <div class="person">
      <p class="person-name">Salem Dabbagh</p>
      <p class="person-title">CEO</p>
      <p class="person-name arabic" lang="ar">سالم دباغ</p>
      <p class="person-title arabic" lang="ar">المدير المفوض</p>
    </div>

    <address class="address">
      Locality 428 - Alley 17 - House 9<br>
      Al Dhaheera - Baghdad - Iraq
    </address>

    <ul class="contacts">
      <li class="contact-item">
        <svg class="contact-icon" viewBox="0 0 24 24"><path fill="var(--brand-blue)" d="M6.6 10.8a15 15 0 0 0 6.6 6.6l2.2-2.2c.3-.3.7-.4 1-.2 1.1.4 2.3.6 3.6.6.6 0 1 .4 1 1V20c0 .6-.4 1-1 1A17 17 0 0 1 3 4c0-.6.4-1 1-1h3.5c.6 0 1 .4 1 1 0 1.3.2 2.5.6 3.6.1.3 0 .7-.2 1z"/></svg>
        <span>014 862 3705</span>
      </li>
      <li class="contact-item">
        <svg class="contact-icon" viewBox="0 0 24 24"><rect x="2" y="5" width="20" height="14" rx="2" fill="var(--brand-blue)"/><path d="M3 6l9 7 9-7" fill="none" stroke="#ffffff" stroke-width="1.6"/></svg>
        <span>ceo@wadialsafeer.com</span>
      </li>
      <li class="contact-item">
        <svg class="contact-icon" viewBox="0 0 24 24"><circle cx="12" cy="12" r="10" fill="var(--brand-blue)"/></svg>
        <span>www.wadialsafeer.com</span>
      </li>
    </ul>
  </section>
</main>
</body>
</html>
```